Kivo4 Website design (Need help to re-design our website)

We need someone to help us re-design our website and launch it. All contents for the website are ready. (Website: https://www.kivo4.com.au/)

-Rearrange categories:
1. Heat Pumps (Link to PALOX site: https://palox.com.au/)
2. Solar (Under the Solar category; remove solar panels, solar inverters, and solar batteries)
3. LED
4. Capability Statement
5. Service and Support
6. Contact us

Home page - redesign but the free quote will stay.

NOTE:
-Try using professional fonts (Example: Helvetica, etc.)
-Try to play with colours related to sustainability, eco-friendliness, solar, energy, and energy efficiency.
-The website's Footer should be readable and use light colour.

Target Market(s)

Residentials & commercial buildings

Industry/Entity Type

SOLAR ENERGY PROVIDER

Coding

Coded - Design and coding required

Colors

Designer to choose colors to be used in the design.

Requirements
Nice to have
• Effects/transition on the words/copy/images.

```html
<!DOCTYPE html>
<html lang="en">
<head>
<meta charset="UTF-8">
<title>Kivo4 – Next Generation Energy Saving Products</title>
<link href="https://fonts.googleapis.com/css2?family=Russo+One&family=Roboto:wght@400;500;700&display=swap" rel="stylesheet">
<style>
:root{
  --green:#5cb531;
  --green-dark:#3f8f1c;
  --lime:#8fd14f;
  --navy:#10203a;
  --ink:#1e2733;
  --text:#5a6470;
  --dark:#141a20;
  --grey:#ececec;
  --light:#f6f7f4;
  --white:#ffffff;
  --faint:#ededed;
}
*{box-sizing:border-box;margin:0;padding:0}
html,body{width:1200px;height:3872px;overflow:hidden}
body{font-family:"Roboto",Arial,sans-serif;color:var(--ink);background:var(--white);position:relative}
h1,h2,h3,.display{font-family:"Russo One","Arial Black",sans-serif;font-weight:400;text-transform:uppercase}
a{color:inherit;text-decoration:none}
.btn{display:inline-block;background:var(--green);color:var(--white);font-size:12px;font-weight:700;text-transform:uppercase;padding:12px 26px;letter-spacing:.5px}
.eyebrow{color:var(--green);font-size:11px;font-weight:700;text-transform:uppercase;letter-spacing:1px}
.photo{display:block}
.brand{display:flex;align-items:center;gap:10px;font-family:"Roboto",Arial,sans-serif;font-weight:700;font-size:30px}
.brand .dot{width:22px;height:22px;border-radius:50%;background:var(--green)}

/* header */
.site-header{position:absolute;top:0;left:0;width:1200px;height:80px;display:flex;align-items:center;justify-content:space-between;padding:0 40px;z-index:3}
.site-header .brand{color:var(--white)}
.main-nav{display:flex;gap:30px;font-size:12px;font-weight:700;color:var(--white);text-transform:uppercase}
.main-nav .active{color:var(--lime)}

/* hero */
.hero{position:absolute;top:0;left:0;width:1200px;height:840px}
.hero .photo{position:absolute;inset:0;width:100%;height:100%;background:linear-gradient(180deg,#2f4a7a 0%,#5a78a8 35%,#8c8f93 60%,#4d5561 80%,#2b3138 100%)}
.hero-copy{position:absolute;top:118px;left:0;width:1200px;text-align:center;color:var(--white)}
.hero-copy h1{font-size:40px;letter-spacing:1px}
.hero-copy p{width:760px;margin:18px auto 0;font-size:14px;line-height:1.6;opacity:.9}
.quote{position:absolute;top:552px;left:120px;width:960px;height:208px;display:flex;box-shadow:0 10px 30px rgba(0,0,0,.25)}
.quote-title{width:392px;background:rgba(20,26,32,.88);color:var(--white);display:flex;align-items:flex-end;padding:0 0 40px 40px}
.quote-title h2{font-size:30px;line-height:1.15}
.quote-form{flex:1;background:var(--white);padding:36px 40px;display:grid;grid-template-columns:1fr 1fr;gap:16px 20px;align-content:start}
.field{height:38px;border:1px solid #d8d8d8;font-size:11px;color:#999;padding:12px}
.quote-foot{grid-column:1/3;display:flex;justify-content:space-between;align-items:center;margin-top:6px}
.social{display:flex;align-items:center;gap:8px;font-size:11px;color:var(--text)}
.social i{width:22px;height:22px;border-radius:50%;background:var(--navy);display:block}
.social.green i{background:var(--green)}

/* who */
.who{position:absolute;top:840px;left:0;width:1200px;height:340px}
.who-copy{position:absolute;left:120px;top:20px;width:440px}
.who-copy h2{font-size:40px;margin:8px 0 14px}
.who-copy p{font-size:12px;line-height:1.6;color:var(--text);margin-bottom:10px}
.who-copy strong{color:var(--ink)}
.who-media{position:absolute;left:600px;top:0;width:480px;height:330px}
.accent{position:absolute;background:var(--green)}
.faint-line{position:absolute;left:0;width:1200px;height:50px;line-height:50px;text-align:center;font-size:46px;color:var(--faint);white-space:nowrap;overflow:hidden}

/* categories */
.categories{position:absolute;top:1232px;left:0;width:1200px;height:440px;background:var(--dark);text-align:center;color:var(--white)}
.categories h2{font-size:36px;margin-top:8px}
.cat-grid{position:absolute;top:140px;left:120px;width:960px;display:flex;gap:20px}
.cat-card{flex:1;height:208px;position:relative}
.cat-card .photo{position:absolute;inset:0}
.cat-card .label{position:absolute;left:26px;bottom:24px;text-align:left}
.cat-card h3{font-size:24px}
.cat-card small{font-size:10px;color:var(--lime);font-weight:700;text-transform:uppercase}

/* services */
.services{position:absolute;top:1672px;left:0;width:1200px;height:520px}
.svc-intro{position:absolute;left:120px;top:100px;width:440px}
.svc-intro h2{font-size:36px;margin:8px 0 14px}
.svc-intro p{font-size:12px;color:var(--text);line-height:1.6;margin-bottom:8px}
.svc-card{position:absolute;width:470px;height:180px;background:var(--white);box-shadow:0 6px 24px rgba(0,0,0,.1);padding:28px 30px}
.num{width:36px;height:36px;border-radius:50%;background:var(--navy);color:var(--white);font-weight:700;display:flex;align-items:center;justify-content:center;font-size:15px;margin-bottom:14px}
.svc-card h3{font-size:18px;margin-bottom:10px}
.svc-card p{font-size:11px;line-height:1.6;color:var(--text)}

/* projects */
.projects{position:absolute;top:2300px;left:0;width:1200px;height:840px;background:var(--grey);text-align:center}
.projects h2{font-size:38px;margin-top:56px}
.proj{position:absolute}

/* reviews */
.reviews{position:absolute;top:3160px;left:0;width:1200px;height:360px;background:var(--light)}
.reviews .photo{position:absolute;left:0;top:0;width:520px;height:360px}
.review-copy{position:absolute;left:600px;top:70px;width:460px}
.review-copy h2{font-size:34px;line-height:1.1;margin:8px 0 16px}
.review-copy p{font-size:12px;line-height:1.6;color:var(--text)}
.review-copy .who-said{margin-top:14px;font-size:11px;color:var(--ink);font-weight:700}
.dots{display:flex;gap:6px;margin-top:24px}
.dots i{width:8px;height:8px;border-radius:50%;background:#c7c7c7}
.dots i:first-child{background:var(--green)}

/* subscribe */
.subscribe{position:absolute;top:3520px;left:0;width:1200px;height:200px;background:linear-gradient(90deg,var(--green-dark),var(--green) 55%,var(--lime))}
.subscribe h2{position:absolute;left:120px;top:56px;font-size:32px;line-height:1.1;color:var(--white)}
.sub-form{position:absolute;left:520px;top:76px;width:600px;display:flex;align-items:center}
.sub-form .field{width:360px;border:none;border-bottom:1px solid rgba(255,255,255,.7);color:rgba(255,255,255,.85);background:transparent}
.sub-form .btn{margin-left:32px;background:var(--white);color:var(--green-dark);padding:14px 46px}

/* footer */
.site-footer{position:absolute;top:3720px;left:0;width:1200px;height:152px;background:var(--white);text-align:center}
.site-footer .brand{justify-content:center;margin-top:22px;color:var(--ink)}
.foot-nav{display:flex;justify-content:center;gap:36px;margin-top:16px;font-size:11px;font-weight:700;text-transform:uppercase;color:var(--ink)}
.foot-bottom{position:absolute;left:40px;right:40px;bottom:14px;display:flex;justify-content:space-between;align-items:center;font-size:10px;color:var(--text)}
.foot-bottom .social i{width:18px;height:18px}
</style>
</head>
<body>

<header class="site-header">
  <a class="brand" href="#"><span class="dot"></span>Kivo4</a>
  <nav class="main-nav">
    <a href="#heat-pumps">Heat Pumps</a>
    <a class="active" href="#solar">Solar</a>
    <a href="#led">LED</a>
    <a href="#capability">Capability Statement</a>
    <a href="#support">Service and Support</a>
    <a href="#contact">Contact Us</a>
  </nav>
</header>

<section class="hero">
  <div class="photo" role="img" aria-label="Modern house with solar panels on a tiled roof under a blue sky"></div>
  <div class="hero-copy">
    <h1>Why pay excess for your electricity?</h1>
    <p>Save on electricity costs by switching to solar. Did you know that you could have a solar system for a lower price than your current electricity bills? If you are paying for electricity, why not pay for greener, cleaner energy? It’s that simple.</p>
  </div>
  <div class="quote">
    <div class="quote-title"><h2>Want a<br>free quote?</h2></div>
    <form class="quote-form">
      <div class="field">Name</div>
      <div class="field">Email</div>
      <div class="field">Phone</div>
      <div class="field">Address</div>
      <div class="quote-foot">
        <span class="btn">Submit</span>
        <span class="social">Follow us here <i></i><i></i><i></i><i></i></span>
      </div>
    </form>
  </div>
</section>

<section class="who">
  <div class="who-copy">
    <span class="eyebrow">About Kivo4</span>
    <h2>Who we are</h2>
    <p>Kivo4 is an Australian owned company with over ten years in energy efficiency, helping homes and businesses reduce their bills with smart renewable solutions that last.</p>
    <p><strong>That’s where we come in!</strong></p>
    <p>We are a sustainability driven local team that specialises in adopting the latest technologies to improve energy efficiency and reduce costs.</p>
    <span class="btn" style="margin-top:10px">Explore More</span>
  </div>
  <div class="who-media">
    <div class="accent" style="left:400px;top:0;width:80px;height:60px"></div>
    <div class="accent" style="left:0;top:260px;width:40px;height:60px"></div>
    <div class="photo" role="img" aria-label="Rows of solar panels under a clear sky" style="position:absolute;left:20px;top:30px;width:260px;height:190px;background:linear-gradient(160deg,#7fa8d8,#2c4f86 70%,#1a2d4d)"></div>
    <div class="photo" role="img" aria-label="Technicians installing solar panels on a roof" style="position:absolute;left:220px;top:130px;width:240px;height:190px;background:linear-gradient(160deg,#a9c8e8,#54708f 55%,#2e3a4a)"></div>
  </div>
</section>

<div class="faint-line display" style="top:1182px">Next generation energy saving products</div>

<section class="categories">
  <div style="padding-top:52px">
    <span class="eyebrow">Browse our range</span>
    <h2>Our solar categories</h2>
  </div>
  <div class="cat-grid">
    <div class="cat-card">
      <div class="photo" role="img" aria-label="Residential rooftop solar panels at sunset" style="background:linear-gradient(180deg,#f0a640,#b5622a 55%,#3a2a22)"></div>
      <div class="label"><h3>Residential Solar</h3><small>Learn more</small></div>
    </div>
    <div class="cat-card">
      <div class="photo" role="img" aria-label="Commercial solar farm on open ground" style="background:linear-gradient(180deg,#7a9fc7,#4b6a8c 50%,#6b5a3e)"></div>
      <div class="label"><h3>Commercial Solar</h3><small>Learn more</small></div>
    </div>
  </div>
  <span class="btn" style="position:absolute;left:540px;top:392px">Explore More</span>
</section>

<section class="services">
  <div class="svc-intro">
    <span class="eyebrow">Get to know us</span>
    <h2>Services we offer</h2>
    <p>Keep your solar energy system running smoothly.</p>
    <p>We provide reliable and professional solar system inspections and repairs.</p>
    <span class="btn" style="margin-top:10px">Explore More</span>
  </div>
  <div class="svc-card" style="left:600px;top:100px">
    <div class="num">1</div>
    <h3>Solar panel cleaning</h3>
    <p>Dust, leaves and bird droppings can reduce panel output. Our regular cleaning restores efficiency so your system keeps producing the power you paid for, all year round.</p>
  </div>
  <div class="svc-card" style="left:120px;top:320px">
    <div class="num">2</div>
    <h3>Solar package repair</h3>
    <p>Faults in wiring, panels or mounts can stop your system working. Our certified technicians find the issue quickly and repair it safely to get you generating again.</p>
  </div>
  <div class="svc-card" style="left:610px;top:320px">
    <div class="num">3</div>
    <h3>Inverter repairs &amp; warranty</h3>
    <p>If your inverter shows errors or has stopped, we test, repair or replace it and handle warranty claims with the manufacturer on your behalf.</p>
  </div>
</section>

<div class="faint-line display" style="top:2230px">Next generation energy saving products</div>

<section class="projects">
  <h2>Our recent projects</h2>
  <div class="proj photo" role="img" aria-label="Ground mounted solar array" style="left:120px;top:112px;width:300px;height:210px;background:linear-gradient(160deg,#8fb4dc,#3c5f8a 60%,#a58a63)"></div>
  <div class="proj photo" role="img" aria-label="Solar panel rows on a commercial roof" style="left:448px;top:112px;width:300px;height:210px;background:linear-gradient(160deg,#9ec1e2,#49698f 60%,#7b7f86)"></div>
  <div class="proj photo" role="img" aria-label="Solar installation beside farmland" style="left:780px;top:112px;width:300px;height:260px;background:linear-gradient(160deg,#a8c6e0,#52769c 55%,#9b7a4f)"></div>
  <div class="proj photo" role="img" aria-label="Industrial shed with rooftop solar" style="left:448px;top:340px;width:300px;height:360px;background:linear-gradient(180deg,#b7cde2,#8a949e 45%,#4e5864)"></div>
  <div class="proj photo" role="img" aria-label="Large flat roof covered in solar panels" style="left:120px;top:512px;width:300px;height:190px;background:linear-gradient(160deg,#a3c3e3,#3e628e 60%,#5d6670)"></div>
  <div class="proj photo" role="img" aria-label="Solar panels on a pitched warehouse roof" style="left:780px;top:512px;width:300px;height:190px;background:linear-gradient(160deg,#9cbde0,#415f85 60%,#6f6a60)"></div>
  <span class="btn" style="position:absolute;left:540px;top:760px">Explore More</span>
</section>

<section class="reviews">
  <div class="photo" role="img" aria-label="Technician working on solar panels at sunset" style="background:linear-gradient(135deg,#f4d7a8,#d79a5c 45%,#8a5a3a)"></div>
  <div class="review-copy">
    <span class="eyebrow">Testimonials</span>
    <h2>Great reviews<br>from our clients</h2>
    <p>All of our lamps are fitted with reliable tracking and temperature controlled monitoring systems so that the transportation of high value and temperature sensitive loads can be monitored at all times.</p>
    <p class="who-said">Client Name<br><span style="font-weight:400;color:var(--text)">Business Owner</span></p>
    <div class="dots"><i></i><i></i><i></i></div>
  </div>
</section>

<section class="subscribe">
  <h2>Subscribe for<br>latest updates</h2>
  <div class="sub-form">
    <div class="field">Enter your email</div>
    <span class="btn">Subscribe</span>
  </div>
</section>

<footer class="site-footer">
  <a class="brand" href="#"><span class="dot"></span>Kivo4</a>
  <nav class="foot-nav">
    <a href="#heat-pumps">Heat Pumps</a>
    <a href="#solar">Solar</a>
    <a href="#led">LED</a>
    <a href="#capability">Capability Statement</a>
    <a href="#support">Service and Support</a>
    <a href="#contact">Contact Us</a>
  </nav>
  <div class="foot-bottom">
    <span>© Copyright 2024 Kivo4. All Rights Reserved.</span>
    <span class="social green"><i></i><i></i><i></i><i></i></span>
  </div>
</footer>

</body>
</html>
```